Lumora Terrain services flyer

We are looking for some eye-catching flyer designs templates for our company lumora terrain pages. We are open to any designs but prefer the theme colour to be similar to our logo colours or something goes well with the colours.
We have attached a pptx that has texts and figures we would like to put on the flyer, please combined slide 1&2 as front page and 3-5 as back page.
Requirements:
Colour theme: similar to logo colours or something that goes well with it (logo is attached)
Page: two sides A4 size
Text & front: No specific requirements
Reference/examples:
- Below website demonstrates how we use our machines for those applications
http://www.brindlecove.example/applications_home.html
- Same applies to slide 11 - 25 from link below
http://www.marcuvelten.example.au/public/documents/5/18/Layered%20Survey%20of%20Bronze%20Ridge%20Basins.pdf

```html
<!DOCTYPE html>
<html lang="en">
<head>
<meta charset="utf-8">
<title>Lumora Terrain services flyer</title>
<link rel="stylesheet" href="https://fonts.googleapis.com/css2?family=Exo+2:wght@500;600&family=Open+Sans:wght@400;600;700&display=swap">
<style>
  :root{
    --bg:#2e2926;
    --paper:#ffffff;
    --orange:#d4532a;
    --orange-light:#e9773d;
    --ink:#3a3a3a;
    --ink-dark:#222;
    --bar-grey:#58585a;
    --photo-earth:#9a6a4c;
    --photo-sky:#4f78b4;
    --photo-core:#8d9198;
  }
  *{box-sizing:border-box;margin:0;padding:0}
  html,body{width:1200px;height:1200px;overflow:hidden;background:var(--bg)}
  body{position:relative;font-family:"Open Sans",sans-serif;color:var(--ink)}
  .page{position:absolute;top:238px;width:558px;height:722px;background:var(--paper);overflow:hidden}
  .page--front{left:28px}
  .page--back{left:614px}

  .brand{position:absolute;left:160px;top:18px;display:flex;align-items:center;gap:8px}
  .brand__mark{width:50px;height:50px;border-radius:50%;background:var(--orange)}
  .brand__name{font-family:"Open Sans",sans-serif;font-weight:700;font-size:17px;line-height:1.05;color:var(--ink-dark);letter-spacing:.5px}

  .banner{position:absolute;color:#fff;font-family:"Exo 2",sans-serif;font-weight:600;font-size:12.5px;
    background:linear-gradient(90deg,var(--orange),var(--orange-light));display:flex;align-items:center;justify-content:center}
  .banner--right{clip-path:polygon(0 12%,94% 12%,94% 0,100% 50%,94% 100%,94% 88%,0 88%)}
  .banner--left{clip-path:polygon(0 50%,6% 0,6% 12%,100% 12%,100% 88%,6% 88%,6% 100%)}

  .ticks{position:absolute;list-style:none;font-size:7.2px;line-height:1.38;text-align:justify}
  .ticks li{position:relative;padding-left:18px;margin-bottom:8px}
  .ticks li::before{content:"";position:absolute;left:1px;top:50%;margin-top:-5px;width:8px;height:8px;border:1.2px solid var(--orange);border-radius:50%}
  .ticks li::after{content:"";position:absolute;left:4.3px;top:50%;margin-top:-3.6px;width:2.2px;height:4.2px;border:solid var(--orange);border-width:0 1.2px 1.2px 0;transform:rotate(45deg)}
  .ticks--tight li{margin-bottom:6.5px}

  .ph{position:absolute}
  .ph--hand{background:linear-gradient(135deg,#6f7d55,#b88a62 60%,#5e4c3c)}
  .ph--core{background:linear-gradient(160deg,#7d8189,var(--photo-core) 50%,#c9c2a8)}
  .ph--field{background:linear-gradient(180deg,var(--photo-sky) 0%,#8fb0d8 38%,var(--photo-earth) 55%,#c9b8a6 100%)}
  .ph--logs{background:#111 linear-gradient(90deg,#0d2a10,#141414 50%,#1b2a40)}
  .ph--section{background:linear-gradient(180deg,#f4f4f4,#dfe8f0 50%,#d9c86a)}
  .ph--table{background:linear-gradient(180deg,#f3efd9,#f0d86a 45%,#c6e2cc)}
  .ph--trench{background:linear-gradient(180deg,#7a8a8f,#86774d 45%,#a75a3a)}
  .ph--model{background:radial-gradient(circle at 45% 50%,#d8392a,#e8a33a 45%,#4aa55b 70%,#fff 72%)}
  .ph--diagram{background:linear-gradient(180deg,#fafafa,#d4d4d4 60%,#f2f2f2);border:1px solid #cfcfcf}
  .ph--framed{border:1px solid #cfcfcf}

  .phone{position:absolute;display:flex;align-items:center;gap:5px;font-family:"Open Sans",sans-serif;font-weight:600;font-size:21px;line-height:1.2;color:var(--ink-dark);letter-spacing:.5px}
  .phone svg{width:15px;height:15px}

  .cta{position:absolute;font-weight:700;font-size:9.6px;line-height:1.25;color:var(--ink-dark);text-align:justify}

  .footer-line{position:absolute;left:0;right:0;bottom:0;height:8px;background:var(--bar-grey)}
  .footer-band{position:absolute;right:0;bottom:0;width:280px;height:32px;background:var(--orange);
    clip-path:polygon(6% 0,100% 0,100% 100%,0 100%);display:flex;align-items:center;justify-content:center;
    color:#fff;font-weight:700;font-size:8.4px;letter-spacing:2.4px;padding-left:14px}
</style>
</head>
<body>

<section class="page page--front">
  <div class="brand">
    <div class="brand__mark"></div>
    <div class="brand__name">NORTHVALE<br>MINERAL INSIGHT</div>
  </div>

  <div class="banner banner--right" style="left:33px;top:86px;width:245px;height:30px;padding-right:30px">Lumora Terrain</div>

  <ul class="ticks" style="left:33px;top:120px;width:234px">
    <li>Northvale Mineral Insight provides a complete lumora terrain service.</li>
    <li>Equipment hire, licencing and logistics to Asia, Africa, Australia, Canada, Europe, Pacific Rim Nations and South America</li>
    <li>PSM / LXR specialists to acquire and validate spectral data from soil, rock chip and downhole samples (chips and core)</li>
    <li>GIS geologists to interpret spectral signatures, develop alteration models and identify mineralisation vectors</li>
    <li>Senior geologists that integrate spectral data with drilling, false-colour imagery (satellite data), lithology, geochemical assays (geochemistry/ assays), geochron, geophysics, radiometrics and structure to generate high-quality exploration targets</li>
    <li>Generative consultants that integrate alteration models and mineralisation vectors with tectonic models, field mapping, mineral distribution intensity and abundance maps, grade shell models and geophysical models to produce new exploration concepts</li>
  </ul>

  <div class="ph ph--hand" style="left:290px;top:90px;width:112px;height:108px" role="img" aria-label="Photo of a handheld spectrometer held against a tree branch"></div>
  <div class="ph ph--core" style="left:412px;top:90px;width:112px;height:108px" role="img" aria-label="Photo of a spectrometer probe scanning drill core in trays"></div>
  <div class="ph ph--field" style="left:290px;top:206px;width:234px;height:107px" role="img" aria-label="Photo of a geologist crouching on a rocky hillside under blue sky"></div>
  <div class="ph ph--logs" style="left:290px;top:322px;width:112px;height:108px" role="img" aria-label="Coloured spectral strip logs on a black background"></div>
  <div class="ph ph--section ph--framed" style="left:412px;top:322px;width:112px;height:108px" role="img" aria-label="Alteration cross-section illustration marked new targets"></div>

  <div class="ph ph--hand" style="left:33px;top:356px;width:112px;height:107px" role="img" aria-label="Photo of a handheld spectrometer held against a tree branch"></div>
  <div class="ph ph--core" style="left:155px;top:356px;width:113px;height:107px" role="img" aria-label="Photo of a spectrometer probe scanning drill core in trays"></div>
  <div class="ph ph--field" style="left:33px;top:471px;width:235px;height:107px" role="img" aria-label="Photo of a geologist crouching on a rocky hillside under blue sky"></div>
  <div class="ph ph--section ph--framed" style="left:33px;top:587px;width:112px;height:107px" role="img" aria-label="Alteration cross-section illustration"></div>
  <div class="ph ph--diagram" style="left:155px;top:587px;width:113px;height:107px" role="img" aria-label="Plan map with circled anomalies marked new discovery"></div>

  <div class="banner banner--left" style="left:282px;top:449px;width:242px;height:27px;padding-left:14px">Lumora Terrain and Earth Imagery</div>

  <ul class="ticks" style="left:290px;top:484px;width:234px">
    <li>Marketing and promotions specialists to draft high impact graphics for public release and to communicate PSM results to investors</li>
    <li>Competent Persons and QAQC systems to report PSM results in accordance with JORC and NI43-101 standards</li>
    <li>And did you know, Northvale Mineral Insight also acquire, process and interpret earth imagery … you can ask us to produce</li>
    <li>ORBIS, TERRAMAP, SKYSCAN, High-resolution drone-acquired Thermal Infrared, Horizon 3, LIDAR and RADAR products for you.</li>
    <li>Need an airborne magnetics, radiometrics and topographic surveys… call or email Northvale Mineral Insight</li>
  </ul>

  <div class="phone" style="left:322px;top:651px">
    <svg viewBox="0 0 24 24"><path fill="none" stroke="#333" stroke-width="2.2" d="M6 3l3 4-2 2c1 3 4 6 7 7l2-2 4 3-2 3C10 20 4 14 3 5z"/></svg>
    +61 7 5550 41 27
  </div>

  <div class="footer-line"></div>
  <div class="footer-band">WWW.NORTHVALEINSIGHT.EXAMPLE</div>
</section>

<section class="page page--back">
  <div class="banner" style="left:33px;top:34px;width:233px;height:21px">Lumora Terrain and Earth Imagery</div>
  <ul class="ticks ticks--tight" style="left:33px;top:66px;width:234px">
    <li>Northvale Mineral Insight provides a complete LUMORA TERRAIN TRAINING service.</li>
    <li>Courses on equipment use, licencing and data interpretation are available to early career geoscientists, senior geologists and exploration managers across Asia, Africa, Australia, Canada, Europe, Pacific Rim Nations and South America</li>
    <li>Learn how PSM / LXR specialists acquire and validate spectral data from soil, rock chip and downhole samples (chips and core)</li>
    <li>Understand how Lumora Terrain geologists interpret PSM / LXR strip logs, develop alteration models and identify mineralisation vectors</li>
  </ul>

  <ul class="ticks ticks--tight" style="left:289px;top:30px;width:236px">
    <li>Meet senior geologists that integrate spectral data with drilling, false-colour imagery (satellite data), lithology, geochemical assays, geochronology, geophysics, radiometrics and structure to generate high-quality exploration targets</li>
    <li>Participate in a case-study where generative consultants integrate alteration models and mineralisation vectors with field mapping, mineral distribution intensity and abundance maps, grade shell models, geophysics and tectonic models to produce new exploration concepts</li>
    <li>See how marketing and promotions specialists incorporate PSM data into high impact graphics for public release and to communicate investment opportunities to market participants and senior management</li>
    <li>Ask our Competent Persons and QAQC experts how to report PSM results in accordance with JORC and NI43-101 standards</li>
  </ul>

  <div class="banner" style="left:33px;top:221px;width:233px;height:21px">Lumora Terrain and Earth Imagery</div>
  <ul class="ticks ticks--tight" style="left:33px;top:254px;width:234px">
    <li>Northvale Mineral Insight provides a complete LUMORA TERRAIN TRAINING service.</li>
    <li>Courses on equipment use, licencing and data interpretation are available to early career geoscientists, senior geologists and exploration managers across Asia, Africa, Australia, Canada, Europe, Pacific Rim Nations and South America</li>
    <li>Learn how PSM / LXR specialists acquire and validate spectral data from soil, rock chip and downhole samples (chips and core)</li>
    <li>Understand how Lumora Terrain geologists interpret PSM / LXR strip logs, develop alteration models and identify mineralisation vectors</li>
    <li>Meet senior geologists that integrate spectral data with drilling, false-colour imagery (satellite data), lithology, geochemical assays, geochronology, geophysics, radiometrics and structure to generate high-quality exploration targets</li>
  </ul>

  <div class="ph ph--table ph--framed" style="left:290px;top:221px;width:112px;height:105px" role="img" aria-label="Mineral temperature stability chart with coloured bands"></div>
  <div class="ph ph--table ph--framed" style="left:414px;top:221px;width:111px;height:105px" role="img" aria-label="Alteration mineral classification table"></div>
  <div class="ph ph--trench" style="left:290px;top:338px;width:112px;height:104px" role="img" aria-label="Photo of a geologist sampling core trays in red soil"></div>
  <div class="ph ph--model ph--framed" style="left:414px;top:338px;width:111px;height:104px" role="img" aria-label="Coloured 3D grade shell model"></div>

  <ul class="ticks" style="left:33px;top:452px;width:492px">
    <li>Participate in a case-study where generative consultants integrate alteration models and mineralisation vectors with field mapping, mineral distribution intensity and abundance maps, grade shell models, geophysics and tectonic models to produce new exploration concepts</li>
  </ul>

  <div class="ph ph--diagram" style="left:32px;top:484px;width:234px;height:99px" role="img" aria-label="Vein long section showing ore shoots and a circled new target"></div>
  <div class="ph ph--diagram" style="left:32px;top:592px;width:234px;height:99px" role="img" aria-label="Mica compositional contour section with outflow arrow and circled new target"></div>

  <div class="banner" style="left:289px;top:484px;width:236px;height:21px">Lumora Terrain and Earth Imagery</div>
  <ul class="ticks ticks--tight" style="left:289px;top:517px;width:236px">
    <li>Northvale Mineral Insight provides a complete LUMORA TERRAIN TRAINING service.</li>
    <li>See how marketing and promotions specialists incorporate PSM data into high impact graphics for public release and to communicate investment opportunities to market participants and senior management</li>
    <li>Ask our Competent Persons and QAQC experts how to report PSM results in accordance with JORC and NI43-101 standards</li>
  </ul>

  <p class="cta" style="left:291px;top:614px;width:234px">Time to train your team and make an exploration breakthrough... call or email Northvale Mineral Insight</p>

  <div class="phone" style="left:322px;top:656px">
    <svg viewBox="0 0 24 24"><path fill="none" stroke="#333" stroke-width="2.2" d="M6 3l3 4-2 2c1 3 4 6 7 7l2-2 4 3-2 3C10 20 4 14 3 5z"/></svg>
    +61 7 5550 41 27
  </div>

  <div class="footer-line"></div>
  <div class="footer-band">WWW.NORTHVALEINSIGHT.EXAMPLE</div>
</section>

</body>
</html>
```